Attorney At Law Card Design

I am an attorney. I need something simple but elegant with nice conservative colors. The design should communicate competence, and confidence. I specialize in Personal Injury and Criminal Defense Work.

Industry/Entity Type

Conservative

Contact Information for Business Card

Delvaqui Law Firm
2837 Harlow Ave.
McAllen, TX 76213

Matías "Matt" Delvaqui
512-437-2619 Tel.
512-437-2614 Fax
512-782-5063 Cell

Justice for All

```html
<!DOCTYPE html>
<html lang="en">
<head>
<meta charset="utf-8">
<title>Delvaqui Law Firm – Business Card</title>
<link rel="stylesheet" href="https://fonts.googleapis.com/css2?family=Montserrat:wght@700&family=Arimo&family=Cabin&family=Lexend:wght@300&display=swap">
<style>
  :root {
    --teal: #146f84;
    --teal-soft: #7fb0bc;
    --paper: #ffffff;
    --ink-light: #ffffff;
  }
  * { margin: 0; padding: 0; box-sizing: border-box; }
  html, body {
    width: 1200px;
    height: 701px;
    overflow: hidden;
    background: var(--paper);
  }
  .card {
    position: relative;
    width: 1200px;
    height: 701px;
    background: var(--paper);
  }
  .crest {
    position: absolute;
    left: 62px;
    top: 106px;
    width: 218px;
    height: 140px;
    border-radius: 40px 40px 60px 60px;
    background: radial-gradient(ellipse at center, rgba(20,111,132,0.45), rgba(20,111,132,0.12) 70%, rgba(20,111,132,0) 100%);
  }
  .info-panel {
    position: absolute;
    left: 320px;
    top: 0;
    width: 587px;
    height: 547px;
    background: var(--teal);
    color: var(--ink-light);
  }
  .firm-name {
    position: absolute;
    left: 0;
    width: 100%;
    top: 72px;
    text-align: center;
    font-family: "Montserrat", sans-serif;
    font-weight: 700;
    font-size: 47px;
    letter-spacing: 0.5px;
  }
  .address {
    position: absolute;
    left: 168px;
    top: 160px;
    font-family: "Arimo", sans-serif;
    font-size: 31px;
    line-height: 37px;
    text-align: center;
  }
  .attorney-name {
    position: absolute;
    left: 61px;
    top: 325px;
    font-family: "Cabin", sans-serif;
    font-size: 37px;
  }
  .contact-lines {
    position: absolute;
    left: 64px;
    top: 390px;
    list-style: none;
    font-family: "Arimo", sans-serif;
    font-size: 29px;
    line-height: 39px;
  }
  .practice-areas {
    position: absolute;
    left: 323px;
    top: 556px;
    list-style: none;
    font-family: "Lexend", sans-serif;
    font-weight: 300;
    font-size: 33px;
    line-height: 37px;
    color: var(--teal);
  }
</style>
</head>
<body>
  <main class="card">
    <div class="crest" role="img" aria-label="Ornamental crest with scales of justice and a sword"></div>

    <section class="info-panel">
      <h1 class="firm-name">DELVAQUI LAW FIRM</h1>
      <p class="address">2837 Harlow Avenue<br>McAllen, TX 76213</p>
      <h2 class="attorney-name" style="font-weight:400">Matías “Matt” Delvaqui</h2>
      <ul class="contact-lines">
        <li>512.437.2619</li>
        <li>Fax 512.437.2614</li>
        <li>Cell Justice For All 512.782.5063</li>
      </ul>
    </section>

    <ul class="practice-areas">
      <li>Personal Injury</li>
      <li>Criminal Defense Work</li>
    </ul>
  </main>
</body>
</html>
```